Quorvane Capital Modern Business Card

We need a modern business card template designed for Quorvane Capital.
Quorvane Capital is a diversified global cryptocurrency investment fund.

The font under the logo: Hiragino Kaku Gothic Pro

Color Hexcode: Main colors white (ffffff) & teal (188383), we are open to adding #fcca46 as an accent

Target Market(s)

Accredited Investors, high net worth individuals and institutional investors

Industry/Entity Type

Investment

Contact Information for Business Card

Contact Information should contain
Name
main phone +1 720 555 0147
cell
email

Font styles to use
Sans Serif
Other font styles liked:
• Hiragino Kaku Gothic Pro

Requirements
Must have
• would like to have icons that identify the contact information
• include our website: www.quorvanecapital.example
• include our Tagline: Diversified Crypto Investment Funds
Nice to have
• Would like to have a simple back side with the logo (without the words) and plenty of space

```html
<!DOCTYPE html>
<html lang="en">
<head>
<meta charset="utf-8">
<title>Quorvane Capital – Business Card</title>
<link rel="stylesheet" href="https://fonts.googleapis.com/css2?family=Arimo:wght@400&family=Noto+Sans+JP:wght@400&display=swap">
<style>
  :root {
    --teal: #517d78;
    --teal-bright: #138080;
    --slate: #585f5c;
    --paper: #ffffff;
    --ink: #111111;
    --ink-soft: #3a3a3a;
  }
  html, body {
    margin: 0;
    padding: 0;
    width: 1200px;
    height: 676px;
    overflow: hidden;
    background: var(--paper);
  }
  .card {
    position: relative;
    width: 1200px;
    height: 676px;
    background: var(--paper);
    overflow: hidden;
    font-family: "Arimo", Arial, sans-serif;
  }
  .card__shapes {
    position: absolute;
    inset: 0;
    width: 1200px;
    height: 676px;
  }
  .brand-name {
    position: absolute;
    left: 347px;
    top: 186px;
    margin: 0;
    font-family: "Noto Sans JP", sans-serif;
    font-weight: 400;
    font-size: 21px;
    line-height: 1;
    letter-spacing: 0.2px;
    color: var(--ink);
    white-space: nowrap;
  }
  .tagline {
    position: absolute;
    left: 618px;
    top: 134px;
    margin: 0;
    font-size: 31px;
    font-weight: 400;
    line-height: 46px;
    color: var(--ink);
  }
  .tagline span { display: block; }
  .tagline span + span { padding-left: 10px; }
  .holder-name {
    position: absolute;
    left: 647px;
    width: 200px;
    top: 259px;
    margin: 0;
    text-align: center;
    font-size: 31px;
    font-weight: 400;
    line-height: 1;
    color: var(--ink);
  }
  .contacts {
    list-style: none;
    margin: 0;
    padding: 0;
  }
  .contact {
    position: absolute;
    left: 487px;
    display: flex;
    align-items: center;
    height: 40px;
    font-size: 31px;
    line-height: 1;
    color: var(--ink);
    white-space: nowrap;
  }
  .contact__icon {
    width: 44px;
    height: 40px;
    flex: none;
  }
  .contact__text { margin-left: 19px; }
  .contact--email { top: 402px; }
  .contact--phone { top: 462px; color: var(--ink-soft); letter-spacing: 1px; }
  .contact--web   { top: 522px; color: var(--ink-soft); }
  .contact--web .contact__text { margin-left: 25px; }
  .contact--cell  { top: 576px; }
</style>
</head>
<body>
<main class="card">
  <svg class="card__shapes" viewBox="0 0 1157 652" preserveAspectRatio="none" aria-hidden="true">
    <defs>
      <linearGradient id="lowerBand" x1="0" y1="0" x2="1" y2="0.35">
        <stop offset="0.15" stop-color="#585f5c"/>
        <stop offset="0.9" stop-color="#138080"/>
      </linearGradient>
      <filter id="softShadow" x="-30%" y="-30%" width="160%" height="160%">
        <feGaussianBlur stdDeviation="6"/>
      </filter>
    </defs>
    <!-- lower left band -->
    <polygon points="150,380 436,380 290,652 150,652" fill="url(#lowerBand)"/>
    <!-- shadow under the fold -->
    <polygon points="138,250 150,250 150,395 430,385 138,395" fill="#000" opacity="0.45" filter="url(#softShadow)"/>
    <!-- upper left triangle -->
    <polygon points="150,0 436,380 150,380" fill="var(--teal)"/>
    <!-- top right wedge -->
    <polygon points="870,4 1157,4 1157,386" fill="var(--teal)"/>
    <!-- bottom right wedge -->
    <polygon points="1147,378 1157,372 1157,652 780,652" fill="var(--teal)"/>
  </svg>

  <p class="brand-name">QUORVANE CAPITAL</p>

  <h1 class="tagline"><span>Diversified Crypto</span><span>Investment Funds</span></h1>

  <p class="holder-name">name</p>

  <ul class="contacts">
    <li class="contact contact--email">
      <svg class="contact__icon" viewBox="0 0 44 40" aria-hidden="true">
        <rect x="2" y="9" width="40" height="24" fill="none" stroke="#333" stroke-width="2"/>
        <polyline points="2,9 22,24 42,9" fill="none" stroke="#333" stroke-width="2"/>
        <polyline points="2,33 17,20 M27,20 42,33" fill="none" stroke="#333" stroke-width="2"/>
        <line x1="27" y1="20" x2="42" y2="33" stroke="#333" stroke-width="2"/>
      </svg>
      <span class="contact__text">number</span>
    </li>
    <li class="contact contact--phone">
      <svg class="contact__icon" viewBox="0 0 44 40" aria-hidden="true">
        <path d="M6 6 C3 10 5 18 12 26 C19 34 27 38 31 36 L35 32 L28 25 L24 28 C20 26 15 21 13 16 L16 12 L10 4 Z" fill="none" stroke="#555" stroke-width="1.8" stroke-linejoin="round"/>
      </svg>
      <span class="contact__text">+1 720 555 0147</span>
    </li>
    <li class="contact contact--web">
      <svg class="contact__icon" viewBox="0 0 44 40" aria-hidden="true">
        <circle cx="21" cy="20" r="18" fill="none" stroke="#333" stroke-width="2"/>
        <ellipse cx="21" cy="20" rx="8" ry="18" fill="none" stroke="var(--teal-bright)" stroke-width="2"/>
        <line x1="21" y1="2" x2="21" y2="38" stroke="var(--teal-bright)" stroke-width="2"/>
        <line x1="3" y1="20" x2="39" y2="20" stroke="var(--teal-bright)" stroke-width="2"/>
        <line x1="6" y1="11" x2="36" y2="11" stroke="var(--teal-bright)" stroke-width="2"/>
        <line x1="6" y1="29" x2="36" y2="29" stroke="var(--teal-bright)" stroke-width="2"/>
      </svg>
      <span class="contact__text">www.quorvanecapital.example</span>
    </li>
    <li class="contact contact--cell">
      <svg class="contact__icon" viewBox="0 0 44 40" aria-hidden="true">
        <rect x="10" y="-4" width="22" height="44" rx="3" fill="#444"/>
        <rect x="13" y="4" width="16" height="14" fill="#fff"/>
      </svg>
      <span class="contact__text">cel</span>
    </li>
  </ul>
</main>
</body>
</html>
```